Music portal needs a sleek mobile app design

We need an innovative, cutting edge design for our mobile app for www.tunelofthub.net . LOFTHUB Music is a platform that lets independent musicians upload and share their music for free. Music lovers can discover new music too.

If you visit the website, you'll get an idea of our brand colors and theme. im attaching the logo and our new discover page layout. We use "din Next LT pro" as our brand font.

We are looking for an app optimized for iOS, but can be used on Android and windows too.

Im looking for a design that flows and navigates with user intuition and is sleek, flat style in nature and has Similar apps are wavecrate, tunebarn and blendsky.

Here are some ideas we like, but please dont copy. Come up with something similar in 'feel'

https://www.folioplace.net/gallery/B-TUNE-UP-Music-application/4421930

https://pixelpost.net/shots/7730582-Music-App

The most important pages/ screens for us are:
- The discover screen
- The login and sign up screens
- The splash screen
- The track player screen
- The use profile page screen
Updates

It seems no design has come close to what I was looking for so I will be requesting a refund and withdrawing this project. Thanks for your effort

Target Market(s)

music, music app, wavecrate, lofthub music, music app design

Colors
f78f20
ffcf3e
ffffff
000000

Requirements
Must have
• a sleek easy to use navigation- please create an account on tunelofthub.net to see how the site works.
Nice to have
• Sleek screen to screen transitions
Should not have
• no 3d designs. Flat design only

```html
<!DOCTYPE html>
<html lang="en">
<head>
<meta charset="UTF-8">
<title>LOFTHUB Music — Splash</title>
<link rel="stylesheet" href="https://fonts.googleapis.com/css2?family=Barlow:wght@400;500&display=swap">
<style>
  :root {
    --orange: #f7941d;
    --orange-text: #f78f20;
    --white: #ffffff;
    --black: #000000;
    --stage-red: #b8321f;
    --stage-amber: #c9822f;
    --stage-green: #3f6a22;
    --stage-dark: #231a12;
  }
  * { margin: 0; padding: 0; box-sizing: border-box; }
  html, body {
    width: 675px;
    height: 1200px;
    overflow: hidden;
    background: var(--black);
  }
  .splash {
    position: relative;
    width: 675px;
    height: 1200px;
    overflow: hidden;
    font-family: "Barlow", "Helvetica Neue", Arial, sans-serif;
    color: var(--white);
  }
  .stage-photo {
    position: absolute;
    inset: 0;
    background:
      radial-gradient(circle at 285px 60px, rgba(255,240,190,0.95) 0 55px, rgba(255,220,150,0) 80px),
      radial-gradient(ellipse 380px 300px at 300px 120px, rgba(205,60,35,0.95), rgba(205,60,35,0) 100%),
      radial-gradient(ellipse 320px 360px at 60px 470px, rgba(214,150,60,0.9), rgba(214,150,60,0) 100%),
      radial-gradient(ellipse 360px 420px at 40px 820px, rgba(70,120,35,0.95), rgba(70,120,35,0) 100%),
      radial-gradient(ellipse 300px 500px at 520px 700px, rgba(60,70,45,0.8), rgba(60,70,45,0) 100%),
      linear-gradient(180deg, #9c2a1c 0%, #7a3a1e 35%, #3e3a1c 65%, var(--stage-dark) 100%);
  }
  .brand-badge {
    position: absolute;
    left: 35px;
    top: 35px;
    width: 124px;
    height: 113px;
    background: var(--black);
    border: 2px solid var(--orange);
    display: flex;
    align-items: center;
    justify-content: center;
    font-size: 20px;
    font-weight: 500;
    letter-spacing: 1px;
    color: var(--orange);
  }
  .headline {
    position: absolute;
    left: 0;
    right: 0;
    top: 528px;
    text-align: center;
    font-size: 57px;
    font-weight: 400;
    line-height: 82px;
    letter-spacing: 0.5px;
    color: var(--white);
  }
  .headline .indent { padding-left: 26px; }
  .tagline {
    position: absolute;
    left: 97px;
    top: 680px;
    font-size: 38px;
    font-weight: 400;
    letter-spacing: 0.3px;
    color: var(--orange-text);
  }
  .cta-button {
    position: absolute;
    left: 183px;
    top: 775px;
    width: 350px;
    height: 77px;
    border-radius: 39px;
    background: var(--orange);
    color: var(--white);
    font-size: 38px;
    font-weight: 400;
    display: flex;
    align-items: center;
    justify-content: center;
    text-decoration: none;
  }
  .site-url {
    position: absolute;
    left: 22px;
    top: 1160px;
    font-size: 20px;
    color: var(--white);
  }
  .footer-brand {
    position: absolute;
    right: 22px;
    top: 1152px;
    font-size: 30px;
    font-weight: 400;
    letter-spacing: 3px;
    color: var(--white);
  }
</style>
</head>
<body>
  <main class="splash">
    <div class="stage-photo" role="img" aria-label="Blurred concert photo of a guitarist singing into a microphone under red, amber and green stage lights"></div>

    <div class="brand-badge">LOFTHUB</div>

    <h1 class="headline"><span class="indent">Share and</span><br>discover new sounds</h1>
    <p class="tagline">Forever Free and Unlimited</p>

    <a class="cta-button" href="#">Explore the new</a>

    <p class="site-url">http://www.tunelofthub.net</p>
    <p class="footer-brand">LOFTHUB</p>
  </main>
</body>
</html>
```